Running Book Cover Design Project

My client has written a book about running and his accomplishments throughout the sport, his story etc. We need to get a cover designed for it. The book will be offered online only, but may later on look at printing a few copies later down the track, so it will need to be a vector graphic so we can resize it easily.

The title of the book is 'Keep Moving Forward', written by Marco Dale Ventunilla from the Philippines.

The idea that we have had for the cover is as follows... We would like the word 'step' so be somehow presented in a step, maybe we could use the shoe tread somehow with the word step in it, or use a step in some way, I will leave it up to you, we are pretty open.

Just think that finding running has changed his life and he wants that represented on the cover somehow with the title standing for both taking one more step with running and a metaphor for life.

Do note that the illustration of the 'foot step' has to be a mid-foot or forefoot landing on the ground instead of a heel strike. Reason being that heel strikes can lead to a lot of injuries; the author is against it as well.

UPDATE: The design should have the runner in summer clothes, with bold fonts, not running up steps as these are marathon type events he is running (attached a new image for inspiration), he should be wearing shoes and clothing similar to the attached images from Kestra
Updates

Changes:

AUTHOR - Paul Terrigo

Sorry about the inclusion of Marco, the author's name should be represented as Paul Terrigo

Still waiting on final approval, apologies!

Target Market(s)

Adults based in south east asia predominantly singapore and the philippines.

Targeted to all those who enjoy inspirational stories or books about running

Industry/Entity Type

Printing

Requirements
Must have
• Running imagery
Shoe/Step IIllustration
Title of Book
Author's Name

```html
<!DOCTYPE html>
<html lang="en">
<head>
<meta charset="utf-8">
<title>Keep Moving Forward — Book Cover</title>
<link rel="stylesheet" href="https://fonts.googleapis.com/css2?family=Poppins:wght@600;700&display=swap">
<style>
  :root {
    --stage: #eef0f3;
    --cover-orange: #f7a51e;
    --stripe-orange: #ee9b14;
    --ink: #111111;
    --shadow: rgba(0, 0, 0, 0.35);
  }
  * { margin: 0; padding: 0; box-sizing: border-box; }
  html, body {
    width: 1200px;
    height: 840px;
    overflow: hidden;
    background: var(--stage);
  }
  .stage {
    position: relative;
    width: 1200px;
    height: 840px;
  }
  .cover {
    position: absolute;
    left: 315px;
    top: 40px;
    width: 570px;
    height: 760px;
    background: var(--cover-orange);
    overflow: hidden;
    font-family: "Poppins", "Century Gothic", sans-serif;
    box-shadow: 0 10px 30px rgba(0, 0, 0, 0.18);
  }
  .cover__lines {
    position: absolute;
    left: 0;
    top: 250px;
    width: 100%;
    height: 440px;
    background: repeating-linear-gradient(
      to bottom,
      var(--cover-orange) 0 3px,
      var(--stripe-orange) 3px 4px
    );
  }
  .cover__post {
    position: absolute;
    left: 110px;
    top: 0;
    width: 12px;
    height: 112px;
    background: var(--ink);
  }
  .title-step {
    position: absolute;
    left: 0;
    top: 0;
    width: 570px;
    height: 260px;
  }
  .title-step__shape { fill: var(--ink); }
  .title {
    color: var(--cover-orange);
    font-weight: 700;
    line-height: 1;
    letter-spacing: -0.02em;
  }
  .title span { position: absolute; white-space: nowrap; }
  .title__keep {
    left: 22px;
    top: 122px;
    font-size: 26px;
  }
  .title__moving {
    left: 16px;
    top: 150px;
    font-size: 84px;
  }
  .title__forward {
    right: 18px;
    top: 62px;
    font-size: 56px;
  }
  .step-photo {
    position: absolute;
    width: 84px;
    height: 84px;
    box-shadow: 4px 4px 8px var(--shadow);
  }
  .step-photo--1 { left: 398px; top: 262px; background: linear-gradient(160deg, #e9eef2, #b98a6c 60%, #2b2b2b); }
  .step-photo--2 { left: 358px; top: 358px; background: linear-gradient(180deg, #8fb2cf, #6f8f4a 55%, #4d5e2f); }
  .step-photo--3 { left: 330px; top: 454px; background: linear-gradient(180deg, #8fb8dc, #b9cfe0 55%, #d8cfb8); }
  .step-photo--4 { left: 306px; top: 550px; background: linear-gradient(180deg, #b7cfe2, #6f7f8c 55%, #3e3a36); }
  .step-photo--5 { left: 276px; top: 652px; width: 96px; height: 96px; background: linear-gradient(180deg, #9ec3e0, #c79a7c 50%, #2a2a2a); }
  .author {
    position: absolute;
    right: 26px;
    top: 646px;
    color: var(--ink);
    font-weight: 700;
    font-size: 19px;
    line-height: 1.2;
  }
  .rule {
    position: absolute;
    left: 0;
    width: 100%;
    background: var(--ink);
  }
  .rule--thin { top: 680px; height: 7px; }
  .rule--base { top: 708px; height: 52px; }
</style>
</head>
<body>
  <main class="stage">
    <section class="cover" aria-label="Book cover: Keep Moving Forward by Paul Terrigo">
      <div class="cover__lines"></div>
      <div class="cover__post"></div>
      <svg class="title-step" viewBox="0 0 570 260" aria-hidden="true">
        <polygon class="title-step__shape" points="0,110 300,110 300,50 570,50 570,250 0,250"/>
      </svg>
      <h1 class="title">
        <span class="title__keep">Keep</span>
        <span class="title__moving">Moving</span>
        <span class="title__forward">Forward</span>
      </h1>
      <div class="rule rule--thin"></div>
      <div class="rule rule--base"></div>
      <p class="author">by Paul Terrigo</p>
      <div class="step-photo step-photo--1" role="img" aria-label="Photo of a runner in sports top and shorts mid-stride"></div>
      <div class="step-photo step-photo--2" role="img" aria-label="Photo of runners on a grassy country trail"></div>
      <div class="step-photo step-photo--3" role="img" aria-label="Photo of a runner on a beach under blue sky"></div>
      <div class="step-photo step-photo--4" role="img" aria-label="Photo of a runner on a waterfront path"></div>
      <div class="step-photo step-photo--5" role="img" aria-label="Photo of a runner in summer running clothes"></div>
    </section>
  </main>
</body>
</html>
```